Copper Heron Bar & Grill Takeout Menu

Please create a takeout menu using the attached dine-in menu.
Take out menu size: Tri-Fold 11x17

Industry/Entity Type

Bar & Grill (Restaurant)

Colors

Designer to choose colors to be used in the design.

Requirements
Must have
• Phone number and website. "Order Online" "Order for Delivery"
Nice to have
• Area on the back of the menu to feature happy hour specials.

```html
<!DOCTYPE html>
<html lang="en">
<head>
<meta charset="utf-8">
<title>Copper Heron Bar &amp; Grill — Takeout Menu</title>
<link rel="stylesheet" href="https://fonts.googleapis.com/css2?family=IM+Fell+English+SC&family=Josefin+Sans:wght@400;600;700&family=Kaushan+Script&display=swap">
<style>
:root{
  --paper:#e2dedb;
  --ink:#1c1a19;
  --copper:#9b4e22;
  --brush:#e06a2e;
  --art-purple:#5a3f9c;
  --art-orange:#d9772f;
  --art-yellow:#e9d735;
}
*{margin:0;padding:0;box-sizing:border-box}
html,body{width:1200px;height:849px;overflow:hidden;background:var(--paper)}
body{font-family:"Josefin Sans",sans-serif;color:var(--ink)}
.menu{position:relative;width:1200px;height:849px;background:var(--paper)}
.abs{position:absolute}

.section-title{left:40px;top:36px;width:360px;text-align:center;font-family:"IM Fell English SC",serif;font-size:30px;line-height:27px;letter-spacing:.5px;z-index:1}
.brush-band{left:34px;top:62px;width:370px;height:32px;background:var(--brush);transform:skewX(-8deg) rotate(-1deg);border-radius:3px 10px 4px 12px;opacity:.92}
.intro{left:41px;top:106px;width:360px;font-size:13.2px;line-height:15.7px}
.intro strong{font-weight:700}
.gluten{left:40px;top:264px;font-family:"Kaushan Script",cursive;font-size:15px;color:var(--copper)}

.item{position:absolute;font-size:13.4px;line-height:17px}
.item-name{font-weight:700;font-size:14.2px;display:flex;align-items:center;gap:4px}
.veg-mark{width:14px;height:17px}
.prices{position:absolute;display:flex;font-weight:700;color:var(--copper);font-size:11.5px}
.price{width:52px;text-align:center;display:flex;flex-direction:column;align-items:center;gap:4px}
.price svg{width:14px;height:14px}

.sub-title{left:515px;top:251px;width:180px;text-align:center;font-family:"IM Fell English SC",serif;font-size:13px;letter-spacing:.5px;z-index:1}
.sub-band{left:515px;top:255px;width:180px;height:11px;background:var(--brush);transform:skewX(-10deg);border-radius:3px 8px}
.handheld-intro{left:425px;top:273px;width:360px;font-size:13.2px;line-height:15.7px}
.handheld{position:absolute;left:425px;width:352px;font-size:13.2px;line-height:15.7px}
.handheld-head{display:flex;align-items:baseline;font-weight:700;font-size:13.8px;margin-bottom:4px}
.handheld-head .leader{flex:1;border-bottom:2px dotted var(--ink);margin:0 3px 3px}

.happy-hour{left:423px;top:623px;width:356px;height:180px;border:4px dashed var(--ink);border-radius:4px;text-align:center}
.happy-hour h2{font-family:"IM Fell English SC",serif;font-weight:400;font-size:24px;margin-top:14px;letter-spacing:1px}
.happy-hour p{font-size:13px;margin-top:2px}

.brand{left:830px;top:240px;width:330px;text-align:center;font-family:"Josefin Sans",sans-serif;font-weight:700;font-size:46px;line-height:52px;color:var(--ink)}
.art{top:481px;width:143px;height:97px;border:1px dashed #8a5a2c}
.art-diners{left:827px;background:linear-gradient(135deg,var(--art-purple),var(--art-orange) 60%,var(--art-yellow))}
.art-delivery{left:998px;background:linear-gradient(135deg,var(--art-yellow),var(--art-orange) 55%,#3a6fb0)}
.order-label{top:592px;font-weight:700;font-size:21px;line-height:23px;color:var(--copper);text-transform:uppercase}
.contact-box{left:808px;top:661px;width:352px;height:99px;border:2px solid var(--ink);text-align:center}
.phone{font-family:"Josefin Sans",sans-serif;font-weight:700;font-size:30px;margin-top:22px}
.web{font-weight:700;font-size:19px;margin-top:2px}
</style>
</head>
<body>
<svg width="0" height="0" style="position:absolute">
  <symbol id="icon-beef" viewBox="0 0 20 20"><path fill="currentColor" d="M2 4c2 0 3 1 4 2h8c1-1 2-2 4-2-1 2-2 3-3 3v5c0 3-2 5-5 5s-5-2-5-5V7C4 7 3 6 2 4z"/></symbol>
  <symbol id="icon-chicken" viewBox="0 0 20 20"><path fill="currentColor" d="M6 2h3v3c2 0 4 1 5 3l3-3 1 2-3 3c0 4-3 7-7 7-2 0-4-1-5-3l3-1c-2-1-3-3-3-5 0-2 1-3 3-4z"/></symbol>
  <symbol id="icon-veg" viewBox="0 0 20 20"><circle cx="10" cy="10" r="8.5" fill="none" stroke="currentColor" stroke-width="1.5"/><path d="M6 7l4 7 4-8" fill="none" stroke="currentColor" stroke-width="1.6"/></symbol>
  <symbol id="veg-v" viewBox="0 0 14 17"><path d="M1 3l5 13L13 1M8 6c1-2 3-3 4-3" fill="none" stroke="#1c1a19" stroke-width="1.6"/></symbol>
</svg>

<main class="menu">
  <div class="abs brush-band"></div>
  <h1 class="abs section-title">Gourmet Burgers<br>&amp; Sandwiches</h1>
  <p class="abs intro">Start with your style and then choose your protein. Our burgers are house made and cooked to your temperature.<br>Our Fresh grilled chicken breast is marinated in house and cooked to perfection. Keep it vegetarian by choosing a vegetarian style along with the Quinoa Lentil Burger. All are served on a potato bun with lettuce, tomato, onion, and your choice of hand cut fries or sweet potato fries.<br><strong>Premium sides available for an up charge + $2</strong></p>
  <p class="abs gluten">Gluten-Free Bun Available Upon Request | $2</p>

  <!-- burgers -->
  <div class="item" style="left:42px;top:312px;width:200px">
    <div class="item-name">Calico Cat <svg class="veg-mark"><use href="#veg-v"/></svg></div>
    Roasted red peppers, red onions, brie cheese, and horseradish aioli.
  </div>
  <div class="prices" style="left:244px;top:313px"><div class="price"><svg><use href="#icon-beef"/></svg>15.00*</div><div class="price"><svg><use href="#icon-chicken"/></svg>14.00</div><div class="price"><svg><use href="#icon-veg"/></svg>13.00</div></div>

  <div class="item" style="left:42px;top:397px;width:200px">
    <div class="item-name">Tiger Cat <svg class="veg-mark"><use href="#veg-v"/></svg></div>
    Cheddar, Monterey Jack, and Provolone
  </div>
  <div class="prices" style="left:244px;top:396px"><div class="price"><svg><use href="#icon-beef"/></svg>15.00*</div><div class="price"><svg><use href="#icon-chicken"/></svg>14.00</div><div class="price"><svg><use href="#icon-veg"/></svg>13.00</div></div>

  <div class="item" style="left:42px;top:465px;width:200px">
    <div class="item-name">Cat Scratch Fever <svg class="veg-mark"><use href="#veg-v"/></svg></div>
    Guacamole, 3 pepper colby jack, pico de gallo, and chipotle mayo.
  </div>
  <div class="prices" style="left:244px;top:463px"><div class="price"><svg><use href="#icon-beef"/></svg>15.50*</div><div class="price"><svg><use href="#icon-chicken"/></svg>14.50</div><div class="price"><svg><use href="#icon-veg"/></svg>13.50</div></div>

  <div class="item" style="left:42px;top:550px;width:200px">
    <div class="item-name">The Fat Cat</div>
    Fried egg*, bacon, cheddar cheese, and garlic aioli.
  </div>
  <div class="prices" style="left:244px;top:549px"><div class="price"><svg><use href="#icon-beef"/></svg>16.00*</div><div class="price"><svg><use href="#icon-chicken"/></svg>15.00</div><div class="price"><svg><use href="#icon-veg"/></svg>14.00</div></div>

  <div class="item" style="left:42px;top:635px;width:200px">
    <div class="item-name">Tabby Cat <svg class="veg-mark"><use href="#veg-v"/></svg></div>
    Melted brie cheese, sliced apple, and citrus aioli.
  </div>
  <div class="prices" style="left:244px;top:634px"><div class="price"><svg><use href="#icon-beef"/></svg>16.50*</div><div class="price"><svg><use href="#icon-chicken"/></svg>15.50</div><div class="price"><svg><use href="#icon-veg"/></svg>14.50</div></div>

  <div class="item" style="left:42px;top:704px;width:205px">
    <div class="item-name">The Sphynx <svg class="veg-mark"><use href="#veg-v"/></svg></div>
    Portobello mushrooms, roasted red peppers, smoked gouda cheese, and roasted garlic aioli.
  </div>
  <div class="prices" style="left:244px;top:703px"><div class="price"><svg><use href="#icon-beef"/></svg>16.50*</div><div class="price"><svg><use href="#icon-chicken"/></svg>15.50</div><div class="price"><svg><use href="#icon-veg"/></svg>14.50</div></div>

  <div class="item" style="left:425px;top:44px;width:200px">
    <div class="item-name">Maine Coon</div>
    Grilled shrimp*, roasted corn, swiss cheese, and roasted garlic aioli.
  </div>
  <div class="prices" style="left:629px;top:42px"><div class="price"><svg><use href="#icon-beef"/></svg>16.50*</div><div class="price"><svg><use href="#icon-chicken"/></svg>15.50</div><div class="price"><svg><use href="#icon-veg"/></svg>14.50</div></div>

  <div class="item" style="left:425px;top:130px;width:230px">
    <div class="item-name">Alley Cat <svg class="veg-mark"><use href="#veg-v"/></svg></div>
    Whats up your alley?<br>Choose a cheese, condiment and one topping.<br>Additional Toppings $1 | Bacon, Egg, Shrimp – $2
  </div>
  <div class="prices" style="left:629px;top:128px"><div class="price"><svg><use href="#icon-beef"/></svg>14.00*</div><div class="price"><svg><use href="#icon-chicken"/></svg>13.00</div><div class="price"><svg><use href="#icon-veg"/></svg>12.00</div></div>

  <!-- handhelds -->
  <div class="abs sub-band"></div>
  <h2 class="abs sub-title">Other Handhelds:</h2>
  <p class="abs handheld-intro">All served with Hand Cut Fries or Sweet Potato Fries.<br>Premium sides available for an up charge +2</p>

  <div class="handheld" style="top:313px">
    <div class="handheld-head"><span>Cat Club</span><span class="leader"></span><span>15</span></div>
    Sliced whole wheat bread with roasted garlic aioli, grilled marinated chicken breast, provolone cheese bacon, lettuce and tomato.
  </div>
  <div class="handheld" style="top:391px">
    <div class="handheld-head"><span>Southwest Melt</span><span class="leader"></span><span>14</span></div>
    Sliced whole wheat bread with roasted garlic aioli,3 pepper colby jack, roasted red peppers and corn.
  </div>
  <div class="handheld" style="top:456px">
    <div class="handheld-head"><span>What’s Gouda?</span><span class="leader"></span><span>14</span></div>
    Sliced whole wheat bread with roasted garlic aioli smoked gouda and provolone cheeses, roasted red peppers and portobello mushrooms.
  </div>
  <div class="handheld" style="top:534px">
    <div class="handheld-head"><span>Westover Melt</span><span class="leader"></span><span>14</span></div>
    Sliced whole wheat bread with roasted garlic aioli, zucchini, portobello mushrooms, red peppers, with melted brie and provolone cheeses,
  </div>

  <section class="abs happy-hour">
    <h2>Happy Hour</h2>
    <p>Happy hour specials...</p>
  </section>

  <!-- cover panel -->
  <div class="abs brand">Copper Heron<br>Bar &amp; Grill</div>
  <div class="abs art art-diners" role="img" aria-label="Painted illustration of diners sharing burgers at a table"></div>
  <div class="abs art art-delivery" role="img" aria-label="Painted illustration of a meal being enjoyed at home"></div>
  <div class="abs order-label" style="left:827px">Order<br>Online</div>
  <div class="abs order-label" style="left:998px">Order for<br>Delivery</div>
  <div class="abs contact-box">
    <div class="phone">703-555-0142</div>
    <div class="web">WWW.COPPERHERONGRILL.COM</div>
  </div>
</main>
</body>
</html>
```